Marwick barber salon has created a lotion and needs help titling.Loma by marwick ?Marwi

The product is for a lotion bottle , my prototype lotion bottle size is an 8oz black lotion bottle with pump. I want the label in florescent green. It should tap into the emotion of potential buyers. The design should say choose me 😀(not literally ). Though the text should be clear and punchy . I.e " the skin multi-vitamin." I'm looking for a designer intrigued by the thought of my lotion. The label should be georgeous,informative, with visuals that immediately convey what my product is and how it works.Not distracting, but clear and punchy, with no expectation of someone to read more than a couple of words.The text should support the visual in a way the visual could not. It seems that nowadays visuals are taking over with very little text. The font,color , or punch of color should be enticing.
So here are some particular ideas of points about the lotion that could possibly be put on back as is done by lotion makers.
.ingredients
.ZNT approved
.portion of proceeds go to bright path fund
.TC circled ( which is for pending trademark)
. I would like the word New in fluorescent on the bottle
.P.O Box address of place of manufacturing product.
. To help skin stay slightly moist,soft,and flexible with a smooth fine grained texture.

its a lotion so I want it available for all

Barber

9bcb3c

• the word" Loma" and By marwick...the word new on the bottle visible

```html
<!DOCTYPE html>
<html lang="en">
<head>
<meta charset="utf-8">
<title>Loma – The Skin Nutri-Blend Lotion by Marwick</title>
<link rel="stylesheet" href="https://fonts.googleapis.com/css2?family=Anton&family=Oswald:wght@600&family=Dancing+Script:wght@600&family=Andika&family=Kaushan+Script&family=Tinos&family=Lato:wght@400&display=swap">
<style>
  :root {
    --fluoro-green: #80d52a;
    --ink: #000000;
    --paper: #ffffff;
    --label-white: #f7f7f7;
  }
  html, body {
    margin: 0;
    padding: 0;
    width: 1200px;
    height: 1200px;
    overflow: hidden;
    background: var(--paper);
  }
  .label {
    position: relative;
    width: 1200px;
    height: 1200px;
    background: var(--paper);
  }
  .label__field {
    position: absolute;
    left: 120px;
    top: 120px;
    width: 960px;
    height: 960px;
    background: var(--fluoro-green);
  }
  .label__new {
    position: absolute;
    left: 204px;
    top: 240px;
    margin: 0;
    font-family: "Anton", sans-serif;
    font-size: 64px;
    line-height: 1;
    color: var(--ink);
    letter-spacing: 1px;
  }
  .badge {
    position: absolute;
    left: 0;
    top: 0;
    width: 1200px;
    height: 1200px;
  }
  .badge__script {
    font-family: "Dancing Script", cursive;
    font-size: 34px;
    fill: var(--ink);
  }
  .badge__title {
    font-family: "Oswald", sans-serif;
    font-weight: 600;
    font-size: 35px;
    fill: var(--ink);
  }
  .label__volume {
    position: absolute;
    left: 0;
    width: 1200px;
    top: 744px;
    margin: 0;
    text-align: center;
    font-family: "Tinos", serif;
    font-size: 15px;
    color: var(--paper);
  }
  .brand-band {
    position: absolute;
    left: 120px;
    top: 782px;
    width: 960px;
    height: 182px;
    background: var(--ink);
    text-align: center;
  }
  .brand-band__name {
    margin: 16px 0 0;
    font-family: "Andika", sans-serif;
    font-weight: 400;
    font-size: 58px;
    line-height: 1.1;
    color: var(--paper);
  }
  .brand-band__tagline {
    margin: 8px 0 0;
    font-family: "Kaushan Script", cursive;
    font-size: 30px;
    letter-spacing: 1px;
    line-height: 1.2;
    color: var(--fluoro-green);
  }
  .brand-band__origin {
    margin: 8px 0 0;
    font-family: "Lato", sans-serif;
    font-size: 18px;
    color: var(--paper);
  }
</style>
</head>
<body>
<main class="label">
  <div class="label__field" role="img" aria-label="Repeating black quatrefoil lattice pattern on fluorescent green"></div>

  <p class="label__new">NEW</p>

  <svg class="badge" viewBox="0 0 1200 1200" role="group" aria-label="Product name badge">
    <path class="badge__frame" fill="#000"
      d="M565,300 C585,340 620,368 665,372 C668,395 690,415 715,420 L715,632 C690,637 668,657 665,680 C620,684 585,700 565,722 C545,700 510,684 465,680 C462,657 440,637 415,632 L415,420 C440,415 462,395 465,372 C510,368 545,340 565,300 Z"/>
    <path class="badge__panel" fill="#f7f7f7"
      transform="translate(565 511) scale(0.84) translate(-565 -511)"
      d="M565,300 C585,340 620,368 665,372 C668,395 690,415 715,420 L715,632 C690,637 668,657 665,680 C620,684 585,700 565,722 C545,700 510,684 465,680 C462,657 440,637 415,632 L415,420 C440,415 462,395 465,372 C510,368 545,340 565,300 Z"/>
    <text class="badge__script" x="595" y="420" text-anchor="middle">Loma</text>
    <text class="badge__title" x="568" y="487" text-anchor="middle">THE SKIN</text>
    <text class="badge__title" x="568" y="537" text-anchor="middle">NUTRI-BLEND</text>
    <text class="badge__script" x="595" y="590" text-anchor="middle">Lotion</text>
  </svg>

  <p class="label__volume">150 ml e 8.5.fl.oz</p>

  <section class="brand-band">
    <h1 class="brand-band__name">By Marwick</h1>
    <p class="brand-band__tagline">Daily lotion.&nbsp; Keeps skin soft, smooth and slightly moist.</p>
    <p class="brand-band__origin">MADE IN AMERICA</p>
  </section>
</main>
</body>
</html>
```